Financial Planning business needs a new Business Card design

We need a business card design for an Australian financial planning business. I am looking for a clean simple design

Target Market(s)

People aged 25-40

Industry/Entity Type

Financial Service

Contact Information for Business Card

On the front of the card we need the following information:
Name: Colin Merrow (First Name Green: #006838 and last name Grey: #414042)
Position: Financial Adviser
Qualifications: BEc(Hons), AdDipFS(FP), Dip FMBM, CFL®
Mobile: 0437 512 604
Email: colin@brightledgeplan.com.au

On the back of the card we need:
Postal address: PO BOX 5307, PERTH BC, WA 6849
Website: www.brightledgeplan.com.au
Text: AFS Licence No. 518760

The fields need to be able to be edited.

Font styles to use
Sans Serif

Requirements
Must have
• Information listed above

```html
<!DOCTYPE html>
<html lang="en">
<head>
<meta charset="utf-8">
<title>Brightledge Plan – Business Card</title>
<link href="https://fonts.googleapis.com/css2?family=Quicksand:wght@400;500;700&display=swap" rel="stylesheet">
<style>
  :root {
    --green: #006838;
    --green-on-dark: #2a9a5c;
    --grey: #414042;
    --card-dark: #3d3d3f;
    --card-light: #f3f3f2;
    --text-light: #e2e2e2;
    --backdrop: #8a8a8a;
  }
  * { box-sizing: border-box; margin: 0; padding: 0; }
  html, body { width: 1200px; height: 747px; overflow: hidden; }
  body {
    background: var(--backdrop);
    font-family: "Quicksand", sans-serif;
    display: flex;
    align-items: center;
    justify-content: center;
    gap: 48px;
  }
  .card {
    width: 520px;
    height: 316px;
    border-radius: 4px;
    box-shadow: 0 6px 18px rgba(0,0,0,0.25);
    position: relative;
  }
  .card--back { background: var(--card-dark); }
  .card--front { background: var(--card-light); }

  .brand-name {
    font-weight: 700;
    letter-spacing: 0.5px;
    text-transform: uppercase;
    line-height: 1;
    white-space: nowrap;
  }
  .card--back .brand-name { position: absolute; left: 56px; top: 84px; font-size: 36px; color: var(--green-on-dark); }
  .card--front .brand-name { position: absolute; left: 48px; top: 64px; font-size: 34px; color: var(--green); }

  .back-details { position: absolute; left: 58px; top: 150px; list-style: none; }
  .back-details li {
    display: flex; align-items: center; gap: 10px;
    font-size: 15px; font-weight: 500; color: var(--text-light);
    margin-bottom: 12px;
  }
  .back-details .licence { color: var(--green-on-dark); font-weight: 700; padding-left: 24px; }
  .back-details svg { width: 14px; height: 14px; flex: none; }

  .person { position: absolute; left: 48px; top: 140px; }
  .person-name { font-size: 24px; font-weight: 700; line-height: 1.1; }
  .person-name .first { color: var(--green); }
  .person-name .last { color: var(--grey); }
  .person-role { font-size: 14px; color: var(--grey); margin-top: 4px; }
  .person-quals { font-size: 14px; font-weight: 500; color: var(--green); margin-top: 8px; }

  .contact { position: absolute; left: 48px; bottom: 34px; display: flex; gap: 28px; list-style: none; }
  .contact li { display: flex; align-items: center; gap: 8px; font-size: 16px; color: var(--grey); font-weight: 500; white-space: nowrap; }
  .contact svg { width: 16px; height: 16px; flex: none; }
</style>
</head>
<body>
  <section class="card card--back" aria-label="Card back">
    <div class="brand-name">Brightledge Plan</div>
    <ul class="back-details">
      <li>
        <svg viewBox="0 0 16 16" aria-hidden="true"><circle cx="8" cy="8" r="7" fill="none" stroke="#2a9a5c" stroke-width="1.5"/><path d="M1 8h14M8 1c-3 3-3 11 0 14M8 1c3 3 3 11 0 14" fill="none" stroke="#2a9a5c" stroke-width="1.2"/></svg>
        PO BOX 5307, PERTH BC, WA 6849
      </li>
      <li>
        <svg viewBox="0 0 16 16" aria-hidden="true"><path d="M8 15s5-5.5 5-9A5 5 0 0 0 3 6c0 3.5 5 9 5 9z" fill="#2a9a5c"/><circle cx="8" cy="6" r="1.8" fill="#3d3d3f"/></svg>
        www.brightledgeplan.com.au
      </li>
      <li class="licence">AFS Licence No. 518760</li>
    </ul>
  </section>

  <section class="card card--front" aria-label="Card front">
    <div class="brand-name">Brightledge Plan</div>
    <div class="person">
      <p class="person-name"><span class="first">Colin</span> <span class="last">Merrow</span></p>
      <p class="person-role">Financial Adviser</p>
      <p class="person-quals">BEc(Hons), AdDipFS(FP), Dip FMBM, CFL®</p>
    </div>
    <ul class="contact">
      <li>
        <svg viewBox="0 0 16 16" aria-hidden="true"><rect x="4" y="1" width="8" height="14" rx="1.5" fill="none" stroke="#006838" stroke-width="1.5"/><line x1="7" y1="12.5" x2="9" y2="12.5" stroke="#006838" stroke-width="1.2"/></svg>
        0437 512 604
      </li>
      <li>
        <svg viewBox="0 0 16 16" aria-hidden="true"><rect x="1" y="3.5" width="14" height="9" fill="#006838"/><path d="M1 3.5l7 5 7-5" fill="none" stroke="#f3f3f2" stroke-width="1.2"/></svg>
        colin@brightledgeplan.com.au
      </li>
    </ul>
  </section>
</body>
</html>
```